Photography Studio Prep Guide Design Needed

I have a prep guide I send to all parents who book a session - It is outdated and ugly. I want a gorgeous, clean, modern upscale look for the brochure I send.

I already have the text and can provide photos for the final design. I want the cover to be clean and upscale and modern, with a happy feel.

Target Market(s)

My clients for an upscale Newborn Photography Studio

Requirements
Must have
• space for my photos, an upscale clean feel
Nice to have
• I love color, but don't want the brochure to look busy. I love cream, white, pale pink.

```html
<!DOCTYPE html>
<html lang="en">
<head>
<meta charset="utf-8">
<title>Newborn Session Prep Guide</title>
<link rel="stylesheet" href="https://fonts.googleapis.com/css2?family=Share+Tech+Mono&family=Montserrat:wght@400;500;600&family=Great+Vibes&display=swap">
<style>
  :root {
    --backdrop: #efe8e2;
    --plum: #7a1548;
    --plum-deep: #5e0f37;
    --cream: #f6f1ec;
    --fur: #efe9e3;
    --white: #ffffff;
    --blush: #e9a596;
    --blush-soft: #f7ddd6;
    --ink: #3a3a3a;
    --label-ink: #6b1a3a;
  }
  * { box-sizing: border-box; margin: 0; padding: 0; }
  html, body {
    width: 1200px; height: 1200px; overflow: hidden;
    background: var(--backdrop);
  }
  .canvas { position: relative; width: 1200px; height: 1200px; }

  .page {
    position: absolute; top: 261px;
    width: 679px; height: 847px;
    transform: scale(0.8); transform-origin: 0 0;
    overflow: hidden;
    box-shadow: 0 6px 22px rgba(60, 30, 30, 0.18);
  }
  .page--cover { left: 42px; background: var(--plum); }
  .page--inside { left: 622px; background: var(--white); }

  .cover-art { display: block; width: 679px; height: 847px; }
  .cover-title {
    font-family: "Share Tech Mono", monospace;
    fill: var(--cream);
  }
  .cover-brand {
    font-family: "Montserrat", sans-serif;
    font-weight: 500;
    fill: var(--blush-soft);
  }

  /* Inside page */
  .frame {
    position: absolute; left: 18px; top: 19px;
    width: 643px; height: 810px;
    border: 2px solid var(--blush);
  }
  .frame-gap {
    position: absolute; left: 258px; top: 14px;
    width: 162px; height: 12px; background: var(--white);
  }
  .crest {
    position: absolute; left: 273px; top: 4px;
    width: 132px; height: 36px; border-radius: 18px;
    background: radial-gradient(ellipse at center, #f3c3b7 0%, #fbe9e4 60%, rgba(255,255,255,0) 100%);
  }
  .inside-title {
    position: absolute; left: 0; top: 46px; width: 679px;
    text-align: center;
    font-family: "Great Vibes", cursive;
    font-size: 30px; color: var(--plum);
  }
  .intro {
    position: absolute; left: 0; top: 90px; width: 679px;
    text-align: center;
    font-family: "Montserrat", sans-serif;
    font-size: 13.5px; line-height: 16.5px; color: var(--ink);
  }
  .section-label {
    position: absolute; left: 20px;
    height: 19px; padding: 0 12px 0 15px;
    background: var(--blush);
    font-family: "Share Tech Mono", monospace;
    font-size: 14px; line-height: 19px; letter-spacing: 1.5px;
    color: var(--label-ink);
  }
  .section-label--nursing { top: 184px; }
  .section-label--feeding { top: 339px; }
  .section-body {
    position: absolute; left: 37px; width: 605px;
    font-family: "Montserrat", sans-serif;
    font-size: 12.2px; line-height: 15.3px;
    color: var(--ink); text-align: justify;
  }
  .section-body--nursing { top: 215px; }
  .section-body--feeding { top: 370px; }
  .section-body strong { font-weight: 600; color: #222; }

  .feature-photo {
    position: absolute; left: 20px; top: 505px;
    width: 639px; height: 310px;
    background: linear-gradient(180deg, #ffffff 0%, #f6f1ea 30%, #eee4d9 65%, #f4eee7 100%);
  }
  .feature-url {
    position: absolute; left: 0; top: 812px; width: 679px;
    text-align: center;
    font-family: "Montserrat", sans-serif;
    font-size: 9px; letter-spacing: 3px; color: rgba(200, 180, 170, 0.55);
  }
</style>
</head>
<body>
<main class="canvas">

  <section class="page page--cover" aria-label="Guide cover">
    <svg class="cover-art" viewBox="0 0 679 847" xmlns="http://www.w3.org/2000/svg">
      <defs>
        <linearGradient id="grass" x1="0" y1="0" x2="1" y2="1">
          <stop offset="0" stop-color="#7f9a4a"/>
          <stop offset="1" stop-color="#5f7e3a"/>
        </linearGradient>
        <radialGradient id="blossom" cx="0.5" cy="0.5" r="0.6">
          <stop offset="0" stop-color="#f0c46a"/>
          <stop offset="0.55" stop-color="#ec8a5c"/>
          <stop offset="1" stop-color="#e8978d"/>
        </radialGradient>
        <radialGradient id="violet" cx="0.45" cy="0.5" r="0.6">
          <stop offset="0" stop-color="#c8b4d8"/>
          <stop offset="0.55" stop-color="#7d3f6e"/>
          <stop offset="1" stop-color="#9a8aab"/>
        </radialGradient>
      </defs>

      <!-- soft fur corners -->
      <path class="fur" fill="var(--fur)" d="M0 0 H300 L0 300 Z"/>
      <path class="fur" fill="var(--fur)" d="M396 0 H679 V283 Z"/>
      <path class="fur" fill="var(--fur)" d="M0 540 L102 642 L0 744 Z"/>
      <path class="fur" fill="var(--fur)" d="M679 540 L577 642 L679 744 Z"/>
      <path fill="var(--white)" d="M0 772 Q0 770 2 770 L105 847 H0 Z"/>
      <path fill="var(--white)" d="M679 772 Q679 770 677 770 L574 847 H679 Z"/>

      <!-- photo tiles -->
      <g transform="rotate(45 347 201)">
        <rect role="img" aria-label="Newborn swaddled in green with a floral bonnet"
              x="217" y="71" width="260" height="260" rx="30"
              fill="url(#grass)"/>
      </g>
      <g transform="rotate(45 132 419)">
        <rect role="img" aria-label="Newborn wrapped in yellow inside a ring of orange and pink flowers"
              x="1" y="288" width="262" height="262" rx="30"
              fill="url(#blossom)" stroke="#f4d9d6" stroke-width="4"/>
      </g>
      <g transform="rotate(45 535 431)">
        <rect role="img" aria-label="Newborn in lavender inside a ring of purple flowers"
              x="404" y="300" width="262" height="262" rx="30"
              fill="url(#violet)" stroke="#e3dbe8" stroke-width="4"/>
      </g>

      <!-- studio name -->
      <circle cx="340" cy="598" r="96" fill="none" stroke="var(--blush-soft)" stroke-width="1.5" opacity="0.8"/>
      <text class="cover-brand" x="340" y="590" text-anchor="middle" font-size="17" letter-spacing="2">CLARA WHITFIELD</text>
      <text class="cover-brand" x="340" y="614" text-anchor="middle" font-size="12" letter-spacing="4">PHOTOGRAPHY</text>

      <!-- title -->
      <text class="cover-title" x="340" y="758" text-anchor="middle" font-size="48" letter-spacing="5">NEWBORN SESSION</text>
      <line x1="132" y1="781" x2="253" y2="781" stroke="var(--cream)" stroke-width="1" opacity="0.7"/>
      <line x1="427" y1="781" x2="548" y2="781" stroke="var(--cream)" stroke-width="1" opacity="0.7"/>
      <text class="cover-title" x="340" y="791" text-anchor="middle" font-size="28" letter-spacing="3">PREP GUIDE</text>
      <text class="cover-brand" x="340" y="825" text-anchor="middle" font-size="10" letter-spacing="3.2" opacity="0.85">www.clarawhitfieldphotography.com</text>
    </svg>
  </section>

  <section class="page page--inside" aria-label="Parent instructions">
    <div class="frame"></div>
    <div class="frame-gap"></div>
    <div class="crest" role="img" aria-label="Small bird and flourish ornament"></div>

    <h1 class="inside-title">Parent Instructions &amp; Preparations</h1>
    <p class="intro">Congratulations on expecting a baby!<br>
      Here are my instructions to ensure a successful newborn photography session.<br>
      Please follow these instructions as closely as possible.</p>

    <h2 class="section-label section-label--nursing">1.NURSING</h2>
    <div class="section-body section-body--nursing">
      <p>If you are nursing, please avoid eating anything spicy (hot sauce, hot peppers, curry, etc.) that might upset baby’s tummy for 24 hours preceding your scheduled session.</p>
      <p>Please if you are breastfeeding do NOT drink caffeine or coffee before your session – I know this is hard but baby will be wired if you have caffeine.</p>
      <p>If you notice baby has a lot of gas after feedings please check with your pediatrician and bring gas drops (Calmadrops or other brand) to your session. The most common reason a baby will not settle for a session is gas pressure/discomfort.</p>
    </div>

    <h2 class="section-label section-label--feeding">2.FEEDING</h2>
    <div class="section-body section-body--feeding">
      <p>Feed the baby as much as possible in the 24 hours preceding your session – this will help minimize the amount baby needs to feed during the session, and will help baby sleep as long and as soundly as possible. Feed baby 2-3 hours before your session and not again until you arrive. This feeding is planned in your session time and it’s not rushed.</p>
      <p><strong>Please bring an extra bottle of formula or breastmilk to the session if possible – sometimes a small amount of milk in a bottle can quickly soothe a baby back to sleep without requiring a full feeding.</strong> I will respect your wishes if you choose not to use a bottle, but please understand we may have to pass on some poses if baby will not settle in position, and I cannot use a bottle to soothe them into the pose.</p>
    </div>

    <div class="feature-photo" role="img" aria-label="Sleeping newborn on a cream blanket holding a striped toy bunny"></div>
    <p class="feature-url">www.clarawhitfieldphotography.com</p>
  </section>

</main>
</body>
</html>
```